New banner for our homepage (IT CLOUD INSPIRED)

We want a new website (head) banner / for our home page.

We are a young IT (Cloud) company so the banner has to contain:
- Our current logo: https://www.qorbanet.nl/wp-content/uploads/2021/03/logo.png

- Our motto: ANALYZE VALIDATE ADVISE

- Some (IT) clouds examples (see examples for inspiration):
https://pxhm.io/kW4bN8r
https://pxhm.io/mR2vLqs
https://pxhm.io/HyB6nTe
https://pxhm.io/wQ9uZkd
https://pxhm.io/3NgRa7v
https://pxhm.io/bX8cWpj
https://pxhm.io/eUUrHyL
https://pxhm.io/tqMwSoo

Requirements
Must have
• We are a young IT (Cloud) company so the banner has to contain:

* The current banner must redesigned completely *
https://www.qorbanet.nl/
* The people on the current banner has te be removed *

https://pxhm.io/kW4bN8r
https://pxhm.io/mR2vLqs
https://pxhm.io/HyB6nTe
https://pxhm.io/wQ9uZkd
https://pxhm.io/3NgRa7v
https://pxhm.io/bX8cWpj
https://pxhm.io/eUUrHyL
https://pxhm.io/tqMwSoo
Nice to have
• * The current banner must redesigned completely *

```html
<!DOCTYPE html>
<html lang="en">
<head>
<meta charset="utf-8">
<title>Qorbanet – Homepage Banner</title>
<link rel="stylesheet" href="https://fonts.googleapis.com/css2?family=Raleway:wght@300;400&display=swap">
<style>
  :root {
    --sky-top: #1c78d2;
    --sky-mid: #3d93d4;
    --sky-low: #6fb0d6;
    --sky-haze: #a9c7da;
    --white: #ffffff;
    --disc: #f4f6fb;
    --cloud-deep: #2f5fc4;
    --cloud-mid: #6c9be6;
    --cloud-light: #dfe8f7;
  }
  html, body {
    margin: 0;
    padding: 0;
    overflow: hidden;
    background: var(--sky-top);
  }
  .banner {
    position: relative;
    width: 1200px;
    height: 1200px;
    overflow: hidden;
    background:
      linear-gradient(135deg, rgba(255,255,255,0) 55%, rgba(200,215,225,0.55) 100%),
      linear-gradient(180deg, var(--sky-top) 0%, var(--sky-mid) 40%, var(--sky-low) 75%, var(--sky-haze) 100%);
    font-family: "Raleway", sans-serif;
    color: var(--white);
  }
  .network {
    position: absolute;
    inset: 0;
  }
  .network .link,
  .network .node,
  .network .hub-ring {
    fill: none;
    stroke: var(--white);
  }
  .network .link { stroke-width: 6; }
  .network .node { stroke-width: 7; }
  .network .hub-ring { stroke-width: 4; }
  .network .hub-disc { fill: var(--disc); }
  .hub-illustration {
    position: absolute;
    left: 360px;
    top: 430px;
    width: 480px;
    height: 340px;
    border-radius: 40px;
    background:
      radial-gradient(ellipse 38% 48% at 52% 50%, var(--cloud-deep) 0%, var(--cloud-mid) 55%, rgba(108,155,230,0) 100%),
      linear-gradient(160deg, var(--cloud-light) 0%, #c9d8f2 50%, var(--cloud-light) 100%);
  }
  .brand {
    position: absolute;
    top: 62px;
    left: 0;
    width: 100%;
    text-align: center;
  }
  .brand-mark {
    display: block;
    width: 38px;
    height: 38px;
    margin: 0 auto 14px;
    border-radius: 50%;
    background: var(--white);
  }
  .brand-name {
    margin: 0;
    font-weight: 300;
    font-size: 52px;
    line-height: 1;
    letter-spacing: 0.5px;
  }
  .brand-motto {
    margin: 6px 0 0;
    font-weight: 400;
    font-size: 19px;
    letter-spacing: 1.5px;
  }
  .tagline {
    position: absolute;
    top: 1044px;
    left: 0;
    width: 100%;
    text-align: center;
    font-weight: 300;
    font-size: 34px;
    letter-spacing: 1px;
    margin: 0;
  }
  .tagline .dot { margin: 0 18px; }
</style>
</head>
<body>
<main class="banner">
  <svg class="network" width="1200" height="1200" viewBox="0 0 1200 1200" aria-hidden="true">
    <line class="link" x1="30" y1="216" x2="196" y2="186"/>
    <line class="link" x1="304" y1="222" x2="400" y2="355"/>
    <line class="link" x1="0" y1="420" x2="272" y2="580"/>
    <line class="link" x1="0" y1="760" x2="272" y2="680"/>
    <line class="link" x1="86" y1="806" x2="320" y2="760"/>
    <line class="link" x1="940" y1="205" x2="840" y2="365"/>
    <line class="link" x1="1078" y1="130" x2="1200" y2="95"/>
    <line class="link" x1="1200" y1="450" x2="930" y2="535"/>
    <line class="link" x1="1172" y1="640" x2="935" y2="660"/>
    <line class="link" x1="1150" y1="836" x2="880" y2="780"/>
    <circle class="node" cx="0" cy="216" r="30"/>
    <circle class="node" cx="262" cy="172" r="66"/>
    <circle class="node" cx="1000" cy="150" r="80"/>
    <circle class="node" cx="1210" cy="630" r="42"/>
    <circle class="node" cx="8" cy="826" r="80"/>
    <circle class="node" cx="1210" cy="860" r="62"/>
    <circle class="hub-ring" cx="600" cy="600" r="340"/>
    <circle class="hub-disc" cx="600" cy="600" r="322"/>
  </svg>

  <div class="hub-illustration" role="img" aria-label="Isometric illustration of a blue cloud connected to stacks of server racks"></div>

  <header class="brand">
    <span class="brand-mark" aria-hidden="true"></span>
    <h1 class="brand-name">Qorbanet</h1>
    <p class="brand-motto">ANALYZE.VALIDATE.ADVISE</p>
  </header>

  <p class="tagline">Analyze<span class="dot">•</span>Validate<span class="dot">•</span>Advise</p>
</main>
</body>
</html>
```